1st promo campaign

We are Brisk Figure & Poise Bureau (brikfpb) a brand new company, this is out first flyer and so it is very special to us. We are a model & talent agency that staffs promotional events. for instance, we provide models for brand promotions, energy drinks, alcohol etc, we also provide talent such as fire blowers , mascots, and much more. Im open to any designs, i would like to see something fresh, attention grabbing but at the same time classy, with an upscale feel. I would also like to offer a 10% discount on the first booking on the flyer. please take a moment to get a feel for us, our website is www.brikfpb.example :) thanks a mill!

Target Market(s)

Businesses/Brands

Industry/Entity Type

It Company

Requirements
Must have
• One page flyer, standard size.

```html
<!DOCTYPE html>
<html lang="en">
<head>
<meta charset="utf-8">
<title>Brisk Figure &amp; Poise Bureau – Promo Flyer</title>
<link rel="stylesheet" href="https://fonts.googleapis.com/css2?family=Cinzel:wght@400&family=Arimo:wght@400;700&display=swap">
<style>
  :root {
    --page-bg: #f3f5f5;
    --wine-dark: #240104;
    --wine: #5e0509;
    --wine-bright: #8e0d16;
    --crimson: #b0101c;
    --band-black: #0b0b0b;
    --band-grey: #6e6e6e;
    --band-grey-dark: #3c3c3c;
    --paper: #f4f5f7;
    --paper-shade: #d3d6dc;
    --ink: #111111;
    --white: #ffffff;
    --brand-pink: #c4254a;
  }
  html, body {
    margin: 0;
    padding: 0;
    width: 1200px;
    height: 900px;
    overflow: hidden;
    background: var(--page-bg);
  }
  .canvas {
    position: relative;
    width: 1200px;
    height: 900px;
    overflow: hidden;
    background: var(--page-bg);
  }
  .flyer {
    position: absolute;
    left: 277px;
    top: 27px;
    width: 661px;
    height: 848px;
    overflow: hidden;
    background: var(--paper);
  }
  .flyer-art {
    position: absolute;
    inset: 0;
    width: 661px;
    height: 848px;
  }
  .headline,
  .offer-badge,
  .agency-intro {
    position: absolute;
    margin: 0;
    transform: translate(-50%, -50%) rotate(-16.5deg);
    transform-origin: center center;
    white-space: nowrap;
    color: var(--white);
  }
  .headline {
    left: 177px;
    top: 318px;
    font-family: "Cinzel", "Trajan Pro", serif;
    font-weight: 400;
    font-size: 26px;
    letter-spacing: 1px;
  }
  .offer-badge {
    left: 236px;
    top: 512px;
    padding: 4px 9px;
    border: 3px solid var(--white);
    font-family: "Arimo", Arial, sans-serif;
    font-weight: 700;
    font-size: 14px;
  }
  .agency-intro {
    left: 326px;
    top: 654px;
    font-family: "Arimo", Arial, sans-serif;
    font-weight: 700;
    font-size: 14px;
    line-height: 28px;
    text-align: center;
  }
  .agency-intro span { display: block; }
  .site-url {
    position: absolute;
    left: 246px;
    top: 786px;
    margin: 0;
    font-family: "Arimo", Arial, sans-serif;
    font-weight: 700;
    font-size: 16px;
    color: var(--ink);
  }
  .brand-name {
    position: absolute;
    left: 480px;
    top: 740px;
    width: 150px;
    margin: 0;
    font-family: "Arimo", Arial, sans-serif;
    font-weight: 700;
    font-size: 15px;
    line-height: 18px;
    color: var(--brand-pink);
  }
</style>
</head>
<body>
<main class="canvas">
  <article class="flyer">
    <svg class="flyer-art" viewBox="0 0 661 848" xmlns="http://www.w3.org/2000/svg">
      <defs>
        <linearGradient id="wine-field" x1="0" y1="0" x2="1" y2="0">
          <stop offset="0" stop-color="var(--wine-dark)"/>
          <stop offset="0.6" stop-color="var(--wine)"/>
          <stop offset="1" stop-color="var(--wine-bright)"/>
        </linearGradient>
        <radialGradient id="portrait-tone" cx="0.72" cy="0.45" r="0.75">
          <stop offset="0" stop-color="#c9323e"/>
          <stop offset="0.45" stop-color="#a5121f"/>
          <stop offset="0.8" stop-color="#7a0a12"/>
          <stop offset="1" stop-color="#5a060c"/>
        </radialGradient>
        <linearGradient id="portrait-skin" x1="0" y1="0" x2="0" y2="1">
          <stop offset="0" stop-color="#e8c2b2" stop-opacity="0"/>
          <stop offset="0.5" stop-color="#e4b9a8" stop-opacity="0.55"/>
          <stop offset="1" stop-color="#f0d2c4" stop-opacity="0.8"/>
        </linearGradient>
        <linearGradient id="event-strip-tone" x1="0" y1="0" x2="1" y2="0">
          <stop offset="0" stop-color="#2a2320"/>
          <stop offset="0.35" stop-color="#222a44"/>
          <stop offset="0.65" stop-color="#1a1c2a"/>
          <stop offset="1" stop-color="#3a1a10"/>
        </linearGradient>
        <linearGradient id="grey-band" x1="0" y1="1" x2="0.15" y2="0">
          <stop offset="0" stop-color="var(--band-grey-dark)"/>
          <stop offset="0.55" stop-color="var(--band-grey)"/>
          <stop offset="1" stop-color="#8a8a8a"/>
        </linearGradient>
        <linearGradient id="paper-tone" x1="0" y1="0" x2="0" y2="1">
          <stop offset="0" stop-color="var(--paper)"/>
          <stop offset="1" stop-color="var(--paper-shade)"/>
        </linearGradient>
      </defs>

      <rect class="paper-field" x="0" y="0" width="661" height="848" fill="url(#paper-tone)"/>
      <polygon class="wine-field" points="0,0 661,0 661,445 0,640" fill="url(#wine-field)"/>

      <polygon class="event-photo-strip" role="img" aria-label="Strip of event photos: bartender pouring drinks, two models in white, fire performer"
               points="0,408 520,254 520,364 0,518" fill="url(#event-strip-tone)"/>
      <polygon class="accent-line" points="0,398 520,244 520,250 0,404" fill="var(--crimson)"/>
      <polygon class="accent-line" points="0,522 520,368 520,374 0,528" fill="var(--crimson)"/>

      <g class="portrait-photo" role="img" aria-label="Portrait of a woman in a red feathered masquerade mask with red lips and a red bead necklace">
        <polygon points="170,0 661,0 661,445 345,538 470,390 300,190" fill="url(#portrait-tone)"/>
        <polygon points="430,200 661,120 661,445 345,538 470,390" fill="url(#portrait-skin)"/>
      </g>

      <polygon class="black-band" points="0,638 661,441 661,473 0,653" fill="var(--band-black)"/>
      <polygon class="grey-band" points="0,653 661,473 661,618 0,815" fill="url(#grey-band)"/>
      <polygon class="black-band" points="0,815 661,618 661,633 0,845" fill="var(--band-black)"/>
    </svg>

    <h1 class="headline">Be above the Rest</h1>
    <p class="offer-badge">10% discount on the first booking</p>

    <p class="agency-intro">
      <span>We are A full-service, nationwide promotional events staffing agency</span>
      <span>BRIKFPB delivers superior excellence in various areas of brand marketing</span>
      <span>including trade shows, customized events, alcohol promotions, multiple city</span>
      <span>promotional tours, costumed &amp; specialized talents, and many more</span>
    </p>

    <p class="brand-name">Brisk Figure &amp; Poise Bureau</p>
    <p class="site-url">www.brikfpb.example</p>
  </article>
</main>
</body>
</html>
```